6x9 Postcard "401k Rollover" to market Individuals to transfer their retirement savings to our firm

Formats: .jpg, .png, .psd, .ai
Dimensions: See uploaded documents

We need a postcard to encourage people 45-65 years olds to transfer their retirement plan assets to our financial advising firm. We have uploaded an example we've been working please feel free to use your artistic license to make it look good images etc. You do not need to copy it word for word, we welcome creativity.

Suggested Wording:

We make it easy to rollover your old 401k

Spread the word! If you or someone you know has a 401k with a former employer or has reached age 59 1/2, consider a 401k rollover

The Marlowe Financial team can help rollover your old 401k

Advantages of a rollover: control over your accounts, more investment options, professional investment management, consolidate and simplify your accounts, guaranteed lifetime income options, help from a team of dedicated advisors

Make the most of your old 401k with a new Rollover IRA, speak with a trusted advisor today, (661)555-0142

If the QWM logo is used it MUST be used with the name "Gerald Pruitt" near it to clearly associate the two. if the words are used they Must be after his name and in all caps like this "Gerald Pruitt, ACCREDITED WEALTH STEWARD TM" [super script TM]. These are rules of the QWM trade mark.

Target Market(s)

Age 45 to 65 with sizable assets in 401k retirement plans

Industry/Entity Type

Investment Advisory

Font styles to use
Serif
Sans Serif
Decorative
Script

Colors

Designer to choose colors to be used in the design.

Requirements
Must have
• The post card MUST contain the following text at least 8pt font:
• Securities offered through Ember Ridge Securities, L.P. Member - NEVOC/TALQ | 4875 North Elm Rd, Ste 120, Lancaster, CA 93536 | 800.555.0173 | CA Ins. Lic. #0K48391, #0713948, #0K52806, #0619427
• Must have website and phone number:
• www.geraldpruittadvisory.example
• (661) 555-0142
Nice to have
• We would like the design to convey: Trust, Safety, Growth, Wealth, Planning, Strength, Stable, Peace of Mind, Time, Classic, Legacy

```html
<!DOCTYPE html>
<html lang="en">
<head>
<meta charset="utf-8">
<title>401k Rollover Postcard</title>
<link rel="stylesheet" href="https://fonts.googleapis.com/css2?family=Roboto+Condensed:wght@700&family=Roboto:wght@400;500;700&family=Montserrat:wght@500;700&display=swap">
<style>
  :root {
    --red: #d0202a;
    --red-dark: #9e1219;
    --ink: #1a1a1a;
    --grey-text: #444;
    --paper: #ffffff;
    --backdrop: #e6e6e6;
    --photo-warm: #8a5a3a;
    --photo-light: #d9c2a8;
  }
  * { margin: 0; padding: 0; box-sizing: border-box; }
  html, body { width: 746px; height: 1200px; overflow: hidden; }
  body { background: var(--backdrop); position: relative; font-family: 'Roboto', Arial, sans-serif; color: var(--ink); }

  .postcard { position: absolute; left: 23px; width: 700px; height: 467px; background: var(--paper); overflow: hidden; box-shadow: 0 2px 8px rgba(0,0,0,.18); }
  .postcard--front { top: 60px; }
  .postcard--back { top: 600px; }
  .postcard svg.art { position: absolute; inset: 0; width: 100%; height: 100%; }

  .headline { position: absolute; left: 27px; top: 140px; font-family: 'Roboto Condensed', 'Arial Narrow', sans-serif; font-weight: 700; font-size: 37px; line-height: 38px; color: var(--paper); }

  .advisor { position: absolute; left: 240px; top: 372px; font-family: 'Montserrat', Arial, sans-serif; color: var(--ink); }
  .advisor__name { font-weight: 500; font-size: 20px; letter-spacing: .3px; line-height: 24px; }
  .advisor__mark { display: flex; align-items: center; margin-top: 6px; gap: 10px; }
  .advisor__badge { font-weight: 500; font-size: 20px; line-height: 24px; }
  .advisor__title { font-weight: 500; font-size: 9px; letter-spacing: 1.6px; line-height: 12px; }
  .advisor__title sup { font-size: 6px; letter-spacing: 0; }

  .back-copy { position: absolute; left: 22px; top: 18px; width: 400px; font-size: 12px; line-height: 15px; }
  .back-copy__title { font-weight: 700; font-size: 24px; line-height: 28px; color: var(--red); margin-bottom: 8px; }
  .back-copy__lead { font-weight: 500; width: 300px; margin-bottom: 16px; }
  .back-copy__team { margin-bottom: 14px; }
  .back-copy__sub { color: var(--red); font-weight: 500; display: inline-block; padding-bottom: 3px; border-bottom: 2px solid var(--red-dark); margin-bottom: 8px; }
  .benefits { list-style: none; margin-bottom: 18px; border-left: 1px solid var(--red); margin-left: 3px; padding-left: 11px; }
  .benefits li { position: relative; line-height: 17px; }
  .benefits li::before { content: ""; position: absolute; left: -15px; top: 6px; width: 7px; height: 7px; border-radius: 50%; background: var(--red); }
  .call { margin-bottom: 3px; }
  .phone { display: flex; align-items: center; gap: 10px; color: var(--red); font-weight: 500; font-size: 19px; line-height: 22px; margin-left: 6px; margin-bottom: 4px; }
  .phone svg { width: 13px; height: 13px; }
  .website { font-size: 11px; margin-left: 6px; margin-bottom: 10px; }
  .note { font-size: 10px; margin-bottom: 8px; }
  .legal { font-size: 7.6px; line-height: 10px; color: var(--grey-text); width: 200px; }
</style>
</head>
<body>

<section class="postcard postcard--front">
  <svg class="art" viewBox="0 0 700 467" preserveAspectRatio="none">
    <defs>
      <linearGradient id="photoTone" x1="0" y1="0" x2="1" y2="1">
        <stop offset="0" stop-color="var(--photo-light)"/>
        <stop offset=".55" stop-color="var(--photo-warm)"/>
        <stop offset="1" stop-color="#c9a98a"/>
      </linearGradient>
      <linearGradient id="silver" x1="0" y1="0" x2="1" y2="0">
        <stop offset="0" stop-color="#f4f4f4"/>
        <stop offset="1" stop-color="#dcdcdc"/>
      </linearGradient>
    </defs>
    <path d="M120 0 L700 0 L700 467 L170 467 Z" fill="url(#silver)"/>
    <path role="img" aria-label="Photo of an advisor reviewing paperwork with a smiling couple at a kitchen table" d="M210 0 L700 0 L700 392 C590 385 470 360 380 320 C310 285 300 200 320 130 C338 70 300 25 210 0 Z" fill="url(#photoTone)"/>
    <path d="M330 312 C430 372 560 392 700 398 L700 436 C560 430 430 410 345 360 Z" fill="var(--red)"/>
    <path d="M0 0 L150 0 C290 60 335 210 305 300 C285 360 240 410 205 467 L0 467 Z" fill="var(--red-dark)"/>
    <path d="M0 0 L140 0 C278 62 322 210 292 300 C272 360 228 410 193 467 L0 467 Z" fill="var(--red)"/>
  </svg>
  <h1 class="headline">We Make It<br>Easy to Rollover<br>Your Old 401k</h1>
  <div class="advisor">
    <div class="advisor__name">GERALD PRUITT</div>
    <div class="advisor__mark">
      <span class="advisor__badge">QWM</span>
      <span class="advisor__title">ACCREDITED<br>WEALTH<br>STEWARD<sup>TM</sup></span>
    </div>
  </div>
</section>

<section class="postcard postcard--back">
  <svg class="art" viewBox="0 0 700 467" preserveAspectRatio="none">
    <defs>
      <linearGradient id="swoosh" x1="0" y1="0" x2="1" y2="0">
        <stop offset="0" stop-color="#ffffff"/>
        <stop offset=".5" stop-color="#eeeeee"/>
        <stop offset="1" stop-color="#cfcfcf"/>
      </linearGradient>
    </defs>
    <path d="M0 60 C150 120 300 70 415 50 L415 300 C300 310 150 290 0 310 Z" fill="url(#swoosh)"/>
    <path d="M0 150 C140 200 280 250 415 210 L415 300 C280 320 140 300 0 310 Z" fill="#e4e4e4" opacity=".7"/>
  </svg>
  <div class="back-copy">
    <h2 class="back-copy__title">SPREAD THE WORD!</h2>
    <p class="back-copy__lead">If You Or Someone You Know Has A 401k With A Former Employer "or" Has Reached Age 59 1/2*, Consider A 401k Rollover</p>
    <p class="back-copy__team">The Gerald Pruitt Financial Team<br>can help rollover your old 401k</p>
    <p class="back-copy__sub">Advantages of a rollover</p>
    <ul class="benefits">
      <li>Control over your accounts</li>
      <li>More investment options</li>
      <li>Professional investment managment</li>
      <li>Consolidate and simplify</li>
      <li>Guaranteed lifetime income options</li>
      <li>Help from a team of dedicated advisors</li>
    </ul>
    <p class="call">Make the most of your old 401k with a new Rollover<br>IRA, speak with a trusted advisor,</p>
    <p class="phone">
      <svg viewBox="0 0 24 24" aria-hidden="true"><circle cx="12" cy="12" r="11" fill="none" stroke="currentColor" stroke-width="2"/><path d="M8 6.5l2 2.5-1.2 1.5c.8 1.7 2 2.9 3.7 3.7l1.5-1.2 2.5 2-1 2c-4.5-.5-8-4-8.5-8.5z" fill="currentColor"/></svg>
      661-555-0142
    </p>
    <p class="website">www.geraldpruittadvisory.example</p>
    <p class="note">*Subject to employer plan lules</p>
    <p class="legal">Securities offered through Ember Ridge Securities, L.P. Member - NEVOC/TALQ | 4875 North Elm Rd, Ste 120, Lancaster, CA 93536 | 800.555.0173 | CA Ins. Lic. #0K48391, #0713948, #0K52806, #0619427</p>
  </div>
</section>

</body>
</html>
```